TAILORED EYECARE AND EYEWEAR
Tailor made for you
We Care About Your Eyecare
Harwell Optometrists is a leading professional Opticians whose focus is on clinical care first and foremost using state of the are equipment followed by supplying design led spectacles and contact lenses. Our website is www.halvornsight.co.uk.
We are looking to have a postcard designed which will market the idea in requirements, this also has to have a poster to match which will be displayed in the store.
Health
Our target audience is adults aged 40 years+, our ethos is about patient care. The practice is both professional, clinical and design led. We must communicate the professionalism, simplicity and care. The Postcard will be personalised, obviously the poster will not.
A postcard which is A5 in size (please see the attached PDF for sizing and what areas to leave blank on the reverse for the address etc.) On the front if using a bleed this needs to be 3mm all round. To make it really tailored we would like to include the patients name on the front, this could be in any true type font as long as you supply a copy of the font, so it really can match in with the design. The Posters we require will be based upon the postcard and can be the same but 2 different sizes one is 60" x 40" portrait and the other 30" x 20" portrait. These all need to be CMYK and at 300DPI.
Postcard size information
Company Logo
Contact Details
Design Brief
Postcard Back Text
Postcard Front Text updated 09-09-11
Optometrist of the year logo
Premium Lens Practice Logo
Tailors Dummy

```html
<!DOCTYPE html>
<html lang="en">
<head>
<meta charset="utf-8">
<title>Harwell Optometrists – Tailored Eyecare and Eyewear</title>
<link href="https://fonts.googleapis.com/css2?family=Comfortaa:wght@400;700&display=swap" rel="stylesheet">
<style>
  :root {
    --bg-dark: #1c1c1c;
    --bg-mid: #5a5a5a;
    --bg-light: #d6d6d6;
    --head-tone: #6e6e6e;
    --head-shadow: #151515;
    --text-white: #ffffff;
    --text-grey: #e4e4e4;
    --brand-blue: #1d4f8f;
    --card-white: #ffffff;
  }
  html, body {
    margin: 0;
    padding: 0;
    overflow: hidden;
  }
  .postcard {
    position: relative;
    width: 1200px;
    height: 835px;
    overflow: hidden;
    font-family: "Comfortaa", sans-serif;
    background:
      radial-gradient(ellipse 700px 520px at 1000px 170px, var(--bg-light) 0%, rgba(170,170,170,0.6) 45%, rgba(0,0,0,0) 100%),
      linear-gradient(100deg, var(--bg-dark) 0%, var(--bg-mid) 45%, #8c8c8c 70%, #3a3a3a 100%);
  }
  .mannequin-head {
    position: absolute;
    left: 0;
    top: 60px;
    width: 430px;
    height: 775px;
    border-radius: 60% 45% 0 0 / 40% 35% 0 0;
    background: radial-gradient(ellipse 260px 380px at 240px 300px, var(--head-tone) 0%, #3c3c3c 55%, var(--head-shadow) 100%);
  }
  .message {
    position: absolute;
    left: 410px;
    top: 215px;
    transform: rotate(-13deg);
    transform-origin: left top;
    text-transform: uppercase;
    white-space: nowrap;
  }
  .headline {
    margin: 0;
    font-size: 44px;
    font-weight: 700;
    line-height: 1.25;
    color: var(--text-white);
  }
  .pitch {
    margin: 80px 0 0 29px;
    font-size: 28px;
    font-weight: 400;
    line-height: 34px;
    color: var(--text-grey);
  }
  .tagline {
    margin: 52px 0 0 -8px;
    font-size: 20px;
    font-weight: 400;
    letter-spacing: 0.5px;
    color: var(--text-grey);
  }
  .brand-card {
    position: absolute;
    right: 0;
    bottom: 0;
    width: 372px;
    height: 247px;
    background: var(--card-white);
    border-top-left-radius: 28px;
    display: flex;
    align-items: center;
    justify-content: center;
    gap: 16px;
  }
  .brand-dot {
    width: 22px;
    height: 22px;
    border-radius: 50%;
    background: var(--brand-blue);
  }
  .brand-name {
    font-size: 30px;
    font-weight: 700;
    line-height: 1.2;
    color: var(--brand-blue);
  }
</style>
</head>
<body>
  <main class="postcard">
    <div class="mannequin-head" role="img" aria-label="Photograph of a grey mannequin head in profile facing right"></div>

    <section class="message">
      <h1 class="headline">Does your optician treat<br>you like a number?</h1>
      <p class="pitch">We don't. We listen and tailor eyecare<br>and eyewear for your needs - that's<br>why our patients keep coming back!</p>
      <p class="tagline">Tailored eyecare and eyewear at Harwell Optometrists</p>
    </section>

    <aside class="brand-card">
      <span class="brand-dot"></span>
      <span class="brand-name">Harwell<br>Optometrists</span>
    </aside>
  </main>
</body>
</html>
```